Astrophotography equipment infographic

Hi! We need an infographic that displays different equipment used for astrophotography. Please see attached for further details.

```html
<!DOCTYPE html>
<html lang="en">
<head>
<meta charset="utf-8">
<title>Astrophotography Equipment – Infographic Design</title>
<link href="https://fonts.googleapis.com/css2?family=Josefin+Sans:wght@400;600&family=Open+Sans:ital,wght@0,400;1,700;1,800&family=Raleway:wght@300;400&display=swap" rel="stylesheet">
<style>
  :root{
    --space:#1f2a2c;
    --cream:#fcefdc;
    --cream-deep:#f1dfc4;
    --crater:#ecd7b8;
    --cloud-dark:#9a8c7a;
    --cloud-mid:#c9b89f;
    --taupe:#7a7061;
    --arm:#f3f1ee;
    --arm-shade:#dcd9d5;
    --num:#b9ab93;
    --ink:#1e2a2b;
    --white:#ffffff;
  }
  html,body{margin:0;padding:0;overflow:hidden;background:var(--cream);}
  .canvas{position:relative;width:1200px;height:1200px;overflow:hidden;background:var(--cream);font-family:"Josefin Sans",sans-serif;}

  .space-band{position:absolute;left:0;top:0;width:1200px;height:600px;background:var(--space);}
  .moon-edge{position:absolute;left:0;top:0;width:260px;height:600px;}
  .side-title{position:absolute;left:82px;top:300px;transform:translate(-50%,-50%) rotate(-90deg);
    font-family:"Josefin Sans",sans-serif;font-weight:400;font-size:25px;line-height:30px;letter-spacing:1px;
    color:var(--ink);text-align:left;white-space:nowrap;}

  .illus{position:absolute;}
  .rocket{left:270px;top:68px;width:80px;height:60px;border-radius:40px 50% 50% 40px;background:linear-gradient(90deg,#6d6d6d00,#8a3a44 55%,#b04656);}
  .astro-top{left:1104px;top:146px;width:56px;height:92px;border-radius:26px;background:linear-gradient(#efe2cc,#c8b596);}
  .astro-box{left:928px;top:492px;width:70px;height:94px;border-radius:30px;background:linear-gradient(#efe2cc,#c8b596);}

  .rings{position:absolute;left:0;top:0;width:1200px;height:600px;}

  .category{position:absolute;top:222px;width:300px;text-align:center;color:var(--white);}
  .category h2{margin:0;font-family:"Josefin Sans",sans-serif;font-weight:400;font-size:18.5px;line-height:22px;letter-spacing:.8px;text-transform:uppercase;}
  .category p{margin:12px 0 0;font-family:"Raleway",sans-serif;font-weight:300;font-size:13.5px;letter-spacing:.2px;}

  .kit{position:absolute;top:318px;width:250px;height:250px;background:var(--taupe);overflow:hidden;}
  .kit svg{position:absolute;left:0;top:0;}
  .kit .step{position:absolute;font-family:"Open Sans",sans-serif;font-style:italic;font-weight:800;font-size:26px;color:var(--num);line-height:1;}
  .kit .label{position:absolute;text-align:center;color:var(--white);font-family:"Open Sans",sans-serif;}
  .kit .label b{display:block;font-style:italic;font-weight:700;font-size:10px;line-height:12px;}
  .kit .label small{display:block;font-size:4.6px;line-height:6px;opacity:.85;}
  .kit .label span{display:block;font-size:7px;line-height:8.6px;margin-top:3px;font-weight:400;}

  .headline{position:absolute;left:0;width:1200px;text-align:center;color:var(--ink);margin:0;font-family:"Josefin Sans",sans-serif;font-weight:400;}
  .headline.main{top:640px;font-size:70px;letter-spacing:3px;}
  .headline.sub{top:885px;font-size:60px;line-height:86px;letter-spacing:3px;}

  .lower-deco{position:absolute;left:0;top:600px;width:1200px;height:600px;}
</style>
</head>
<body>
<div class="canvas">

  <div class="space-band"></div>

  <svg class="lower-deco" viewBox="0 600 1200 600" width="1200" height="600" aria-hidden="true">
    <circle cx="40" cy="800" r="45" fill="var(--crater)"/>
    <circle cx="950" cy="845" r="30" fill="var(--crater)"/>
    <circle cx="1150" cy="890" r="58" fill="var(--crater)"/>
    <circle cx="175" cy="985" r="30" fill="var(--crater)"/>
    <circle cx="258" cy="990" r="23" fill="var(--crater)"/>
  </svg>
  <svg class="illus" style="left:0;top:1080px" width="1200" height="120" viewBox="0 0 1200 120" role="img" aria-label="Layered paper-cut clouds along the bottom edge">
    <defs><linearGradient id="cloudGrad" x1="0" y1="0" x2="0" y2="1"><stop offset="0" stop-color="var(--cloud-mid)"/><stop offset="1" stop-color="var(--cloud-dark)"/></linearGradient></defs>
    <path d="M0 20 Q150 50 300 80 Q600 110 900 80 Q1050 60 1200 30 V120 H0 Z" fill="url(#cloudGrad)"/>
  </svg>

  <svg class="moon-edge" viewBox="0 0 260 600" aria-hidden="true">
    <path d="M0 0 H150 Q185 90 178 200 Q172 320 175 420 Q178 520 60 600 H0 Z" fill="var(--cream)"/>
    <circle cx="32" cy="150" r="9" fill="var(--crater)"/>
    <circle cx="92" cy="430" r="9" fill="var(--crater)"/>
    <circle cx="18" cy="495" r="20" fill="var(--crater)"/>
  </svg>
  <div class="illus" style="left:110px;top:0;width:130px;height:150px;border-radius:0 0 70px 60px;background:linear-gradient(90deg,var(--cloud-mid),var(--cloud-dark))" role="img" aria-label="Paper-cut rocket exhaust clouds"></div>
  <div class="illus" style="left:70px;top:440px;width:150px;height:160px;border-radius:70px 70px 0 0;background:linear-gradient(90deg,var(--cloud-mid),var(--cloud-dark))" role="img" aria-label="Paper-cut clouds at the edge of the moon"></div>

  <div class="side-title">ASTROPHOTOGRAPHY<br>EQUIPMENT</div>

  <div class="illus rocket" role="img" aria-label="Small red rocket flying with an exhaust trail"></div>
  <div class="illus astro-top" role="img" aria-label="Floating astronaut"></div>

  <svg class="rings" viewBox="0 0 1200 600" aria-hidden="true">
    <g fill="none" stroke="var(--white)" stroke-width="1.4">
      <circle cx="466" cy="104" r="78"/>
      <circle cx="744" cy="104" r="78"/>
      <circle cx="1022" cy="104" r="78"/>
      <path d="M466 182 V212 M428 212 H504 M744 182 V212 M706 212 H782 M1022 182 V212 M984 212 H1060"/>
    </g>
    <g fill="var(--cream)">
      <circle cx="466" cy="104" r="64"/><circle cx="744" cy="104" r="64"/><circle cx="1022" cy="104" r="64"/>
    </g>
    <g fill="var(--white)">
      <circle cx="466" cy="26" r="4"/><circle cx="410" cy="49" r="4"/><circle cx="522" cy="49" r="4"/><circle cx="466" cy="184" r="4"/>
      <circle cx="744" cy="26" r="4"/><circle cx="688" cy="49" r="4"/><circle cx="800" cy="49" r="4"/><circle cx="688" cy="159" r="4"/><circle cx="800" cy="159" r="4"/><circle cx="744" cy="184" r="4"/>
      <circle cx="1022" cy="26" r="4"/><circle cx="1022" cy="184" r="4"/>
    </g>
    <g font-family="Josefin Sans, sans-serif" font-weight="600" font-size="66" fill="var(--ink)" text-anchor="middle">
      <text x="466" y="128">01</text><text x="744" y="128">02</text><text x="1022" y="128">03</text>
    </g>
  </svg>

  <div class="category" style="left:316px">
    <h2>Landscape<br>Astrophotography</h2>
    <p>EX: Capturing The Milky Way Above A Landscape</p>
  </div>
  <div class="category" style="left:594px">
    <h2>Deep Sky<br>Astrophotography</h2>
    <p>EX: galaxies, nebulae etc</p>
  </div>
  <div class="category" style="left:872px">
    <h2>Solar System<br>Astrophotography</h2>
    <p>EX: sun, moon, saturn, jupiter and other planets</p>
  </div>

  <!-- Landscape kit -->
  <div class="kit" style="left:324px">
    <svg width="250" height="250" viewBox="0 0 250 250" aria-hidden="true">
      <g fill="var(--arm)">
        <polygon points="72,0 98,16 125,0 125,125 72,125"/>
        <polygon points="125,72 250,72 234,98 250,125 125,125"/>
        <polygon points="125,125 178,125 178,250 152,234 125,250"/>
        <polygon points="0,125 125,125 125,178 0,178 16,152"/>
      </g>
      <g fill="var(--arm-shade)">
        <polygon points="125,40 140,52 125,64"/>
        <polygon points="210,125 198,140 186,125"/>
        <polygon points="125,210 110,198 125,186"/>
        <polygon points="40,125 52,110 64,125"/>
      </g>
    </svg>
    <div class="step" style="left:82px;top:90px">01</div>
    <div class="step" style="left:131px;top:90px">02</div>
    <div class="step" style="left:82px;top:138px">04</div>
    <div class="step" style="left:131px;top:138px">03</div>
    <div class="label" style="left:2px;top:12px;width:68px"><b>Regular<br>DSLR camera</b><small>or mirrorless interchangeable lens camera</small><span>A camera with a full-frame sensor is best, but not required.</span></div>
    <div class="label" style="left:140px;top:8px;width:100px"><b>Wide<br>angle lens</b><span>35mm for a full-frame camera, 24mm or below for an APS-C sensor camera</span></div>
    <div class="label" style="left:184px;top:162px;width:62px"><b>Tripod</b><span>the sturdier the better</span></div>
    <div class="label" style="left:2px;top:182px;width:118px"><b>Star tracker<br>(optional)</b><span style="font-size:5.4px;line-height:6.6px">These sit between a camera and tripod and move the camera with the rotation of the earth allowing longer exposures without star trails appearing</span></div>
  </div>

  <!-- Deep sky kit -->
  <div class="kit" style="left:617px">
    <svg width="250" height="250" viewBox="0 0 250 250" aria-hidden="true">
      <g fill="var(--arm)">
        <polygon points="72,0 98,16 125,0 125,125 72,125"/>
        <polygon points="125,72 250,72 234,98 250,125 125,125"/>
        <polygon points="125,125 178,125 178,250 152,234 125,250"/>
        <polygon points="0,125 125,125 125,178 0,178 16,152"/>
      </g>
      <g fill="var(--arm-shade)">
        <polygon points="125,40 140,52 125,64"/>
        <polygon points="210,125 198,140 186,125"/>
        <polygon points="125,210 110,198 125,186"/>
        <polygon points="40,125 52,110 64,125"/>
      </g>
    </svg>
    <div class="step" style="left:82px;top:90px">01</div>
    <div class="step" style="left:131px;top:90px">02</div>
    <div class="step" style="left:82px;top:138px">04</div>
    <div class="step" style="left:131px;top:138px">03</div>
    <div class="label" style="left:2px;top:20px;width:68px"><b>Regular<br>DSLR camera</b><span>or mirrorless interchangeable lens camera</span></div>
    <div class="label" style="left:160px;top:16px;width:80px"><b>Telephoto<br>lens</b><span>85mm to 300mm</span></div>
    <div class="label" style="left:184px;top:162px;width:62px"><b>Tripod</b><span>the sturdier the better</span></div>
    <div class="label" style="left:2px;top:190px;width:118px"><b>Star tracker<br>(optional)</b></div>
  </div>

  <!-- Solar system kit -->
  <div class="kit" style="left:910px">
    <svg width="250" height="250" viewBox="0 0 250 250" aria-hidden="true">
      <g fill="var(--arm)">
        <polygon points="72,0 98,16 125,0 125,125 72,125"/>
        <polygon points="125,72 250,72 234,98 250,125 125,125"/>
        <polygon points="125,125 178,125 178,250 152,234 125,250"/>
        <polygon points="0,125 125,125 125,178 0,178 16,152"/>
      </g>
      <g fill="var(--arm-shade)">
        <polygon points="125,40 140,52 125,64"/>
        <polygon points="210,125 198,140 186,125"/>
        <polygon points="125,210 110,198 125,186"/>
      </g>
    </svg>
    <div class="step" style="left:82px;top:90px">01</div>
    <div class="step" style="left:131px;top:90px">02</div>
    <div class="step" style="left:131px;top:138px">03</div>
    <div class="label" style="left:2px;top:12px;width:68px"><b style="font-size:7px;line-height:8px">Specialist astrophotography camera</b><span style="font-size:5.4px;line-height:6.6px">camera (e.g. CCD camera) or adapted DSLR camera with IR filter</span></div>
    <div class="label" style="left:178px;top:14px;width:68px"><b>Telescope</b><span style="font-size:5.4px;line-height:6.6px">with the camera attached this works in place of a camera lens</span></div>
    <div class="label" style="left:184px;top:158px;width:62px"><b>Tripod</b><span>the sturdier the better</span></div>
  </div>
  <div class="illus astro-box" role="img" aria-label="Floating astronaut"></div>

  <h1 class="headline main">INFOGRAPHIC DESIGN</h1>
  <p class="headline sub">ASTROPHOTOGRAPHY<br>EQUIPMENT</p>

</div>
</body>
</html>
```